Inspirational Quotes Poster Set

Braxlune is a stylish coworking space, which has a design-oriented vintage look from the 60's with an industrial touch (www.braxlune-example.com) Braxlune Quote Poster Set of 16 posters. The poster should be typo oriented and rather simple. Reflecting a bit the clean billboard design from the sixties. Minimal / simple graphical elements

Target Market(s)

Startups and Entrepreneurs

Industry/Entity Type

Startup

Font styles to use
Sans Serif

Colors

Designer to choose colors to be used in the design.

Requirements
Must have
• Posters need to be on and very stylish

```html
<!DOCTYPE html>
<html lang="en">
<head>
<meta charset="utf-8">
<title>Braxlune Quote Poster</title>
<link rel="stylesheet" href="https://fonts.googleapis.com/css2?family=Archivo+Black&family=Archivo:wght@500&display=swap">
<style>
  :root {
    --paper: #fdf7ec;
    --ink: #111111;
    --sun: #fdc82f;
  }
  html, body {
    margin: 0;
    padding: 0;
    overflow: hidden;
    background: var(--paper);
  }
  .poster {
    position: relative;
    width: 849px;
    height: 1200px;
    background: var(--paper);
    overflow: hidden;
  }
  .quote-art {
    position: absolute;
    inset: 0;
  }
  .quote-line {
    font-family: "Archivo Black", "Arial Black", sans-serif;
    fill: var(--ink);
    text-transform: uppercase;
  }
  .quote-line.accent { fill: var(--sun); }
  .mark-open { fill: var(--sun); }
  .mark-close { fill: var(--ink); }
  .highlight-band { fill: var(--sun); }
  .attribution {
    position: absolute;
    left: 333px;
    top: 884px;
    margin: 0;
    font-family: "Archivo", "Helvetica Neue", sans-serif;
    font-weight: 500;
    font-variant: small-caps;
    font-size: 40px;
    line-height: 52px;
    letter-spacing: -1.5px;
    color: var(--ink);
  }
  .attribution .role {
    display: block;
    padding-left: 33px;
  }
  .brand {
    position: absolute;
    left: 640px;
    top: 1138px;
    display: flex;
    align-items: center;
    gap: 8px;
  }
  .brand-square {
    width: 22px;
    height: 22px;
    background: var(--sun);
  }
  .brand-name {
    font-family: "Archivo Black", "Arial Black", sans-serif;
    font-size: 30px;
    line-height: 1;
    color: var(--ink);
    letter-spacing: -1px;
  }
</style>
</head>
<body>
  <main class="poster">
    <svg class="quote-art" width="849" height="1200" viewBox="0 0 849 1200" role="img" aria-label="Ideas are commodity. Execution of them is not.">
      <g class="mark-open">
        <path d="M88,200 V165 Q88,135 125,128 L128,140 Q108,146 106,160 H128 V200 Z"/>
        <path d="M136,200 V165 Q136,135 173,128 L176,140 Q156,146 154,160 H176 V200 Z"/>
      </g>
      <text class="quote-line" x="222" y="224" font-size="122" textLength="322" lengthAdjust="spacingAndGlyphs">Ideas</text>
      <text class="quote-line" x="262" y="301" font-size="80" textLength="146" lengthAdjust="spacingAndGlyphs">Are</text>
      <text class="quote-line" x="102" y="400" font-size="116" textLength="692" lengthAdjust="spacingAndGlyphs">Commodity.</text>
      <rect class="highlight-band" x="82" y="422" width="709" height="135"/>
      <text class="quote-line" x="134" y="528" font-size="112" textLength="604" lengthAdjust="spacingAndGlyphs">Execution</text>
      <text class="quote-line" x="138" y="632" font-size="66" textLength="76" lengthAdjust="spacingAndGlyphs">Of</text>
      <text class="quote-line" x="230" y="662" font-size="114" textLength="300" lengthAdjust="spacingAndGlyphs">Them</text>
      <text class="quote-line" x="318" y="742" font-size="74" textLength="56" lengthAdjust="spacingAndGlyphs">Is</text>
      <text class="quote-line accent" x="400" y="758" font-size="114" textLength="252" lengthAdjust="spacingAndGlyphs">Not.</text>
      <g class="mark-close">
        <path d="M676,748 H716 V783 Q716,805 680,808 L677,797 Q694,793 697,780 H676 Z"/>
        <path d="M720,748 H760 V783 Q760,805 724,808 L721,797 Q738,793 741,780 H720 Z"/>
      </g>
    </svg>

    <p class="attribution">
      <span class="name">Marcus Delane,</span>
      <span class="role">Delane Chairman and CEO</span>
    </p>

    <div class="brand">
      <span class="brand-square"></span>
      <span class="brand-name">braxlune</span>
    </div>
  </main>
</body>
</html>
```